Amber Ridge Productions

I need a business card design for a new freelance film production company using or incorporating the logo:
I want the card to be creative, minimal, yet professional. Feel free to use a variety of different shapes and sizes/ textures for the card.

Industry/Entity Type

Film Production

```html
<!DOCTYPE html>
<html lang="en">
<head>
<meta charset="utf-8">
<title>Amber Ridge Productions – Round Business Card</title>
<link href="https://fonts.googleapis.com/css2?family=Open+Sans:wght@400;600;700&display=swap" rel="stylesheet">
<style>
  :root {
    --page-bg: #ffffff;
    --card-white: #ffffff;
    --brand-blue: #1457a3;
    --text-white: #ffffff;
    --reflection: #8c8fd8;
    --card-shadow: rgba(0, 0, 0, 0.28);
  }
  html, body {
    margin: 0;
    padding: 0;
    overflow: hidden;
    background: var(--page-bg);
  }
  .canvas {
    position: relative;
    width: 1200px;
    height: 848px;
    background: var(--page-bg);
    font-family: "Open Sans", Arial, sans-serif;
  }
  .card {
    position: absolute;
    width: 286px;
    height: 286px;
    border-radius: 50%;
    background: var(--card-white);
    box-shadow: 6px 10px 14px var(--card-shadow);
  }
  .card--front { left: 238px; top: 272px; }
  .card--back  { left: 647px; top: 267px; }

  .brand-name {
    position: absolute;
    left: 0;
    right: 0;
    top: 150px;
    text-align: center;
    color: var(--brand-blue);
    font-weight: 400;
    line-height: 1;
  }
  .brand-name__main {
    display: block;
    font-size: 23px;
    letter-spacing: 0.5px;
  }
  .brand-name__sub {
    display: block;
    margin-top: 5px;
    font-size: 7px;
    letter-spacing: 3.6px;
  }
  .brand-mark {
    position: absolute;
    left: 127px;
    top: 112px;
    width: 32px;
    height: 32px;
    background: var(--brand-blue);
  }
  .back-art {
    position: absolute;
    left: 0;
    top: 0;
  }
  .contact-line {
    fill: var(--text-white);
    font-size: 12px;
    font-weight: 600;
  }
  .holder-name {
    fill: var(--text-white);
    font-size: 17px;
    font-weight: 700;
  }
  .holder-name--reflection {
    fill: var(--reflection);
  }
</style>
</head>
<body>
  <main class="canvas">
    <section class="card card--front" aria-label="Card front">
      <div class="brand-mark"></div>
      <div class="brand-name">
        <span class="brand-name__main">AMBER RIDGE</span>
        <span class="brand-name__sub">PRODUCTIONS</span>
      </div>
    </section>

    <section class="card card--back" aria-label="Card back">
      <svg class="back-art" width="286" height="286" viewBox="0 0 286 286">
        <defs>
          <path id="contact-ring" d="M143 251 A108 108 0 1 1 143 35 A108 108 0 1 1 143 251"/>
        </defs>
        <circle class="back-disc" cx="143" cy="143" r="122" fill="var(--brand-blue)"/>

        <text class="contact-line"><textPath href="#contact-ring" startOffset="50">E: nora@amberridge.com</textPath></text>
        <text class="contact-line"><textPath href="#contact-ring" startOffset="222">www.amberridge.com</textPath></text>
        <text class="contact-line"><textPath href="#contact-ring" startOffset="430">T: 5550 1234</textPath></text>
        <text class="contact-line"><textPath href="#contact-ring" startOffset="532">2/18 dune street</textPath></text>

        <text class="holder-name" x="143" y="148" text-anchor="middle">NORA VALE</text>
        <text class="holder-name holder-name--reflection" x="143" y="-150" text-anchor="middle" transform="scale(1,-1)">NORA VALE</text>
      </svg>
    </section>
  </main>
</body>
</html>
```